THE MARKETPLACE FOR WAREHOUSE, the new way of doing logistics

We need an avant-garde, modern, minimalist and elegant web design for our company called VORDEN. This company represents the future of logistics, where users can find multiple offers of spaces (warehouse) in one place and other users can offer their available spaces to generate an extra cash inflow. A sample of this company is www.plindo-example.com, a US company that has developed this business. The closest thing to this type of business is NESTLOO, since it develops a similar model for people who offer spaces in their homes and people who need a space for a limited time. My domain site is www.vorden-example.com, where is the logo of my company. spanish- ------------------------------------------------ ---------------------------------------------- We need a web design avant-garde, modern, minimalist and elegant for our company called VORDEN. This company represents the future of logistics, where users can find multiple offers of spaces (wineries) in one place and other users can offer their available spaces to generate an extra profit. A sample of this company is www.plindo-example.com, a US company that has developed this business. The closest thing to this type of business is NESTLOO, since it develops a similar model for people who offer spaces in their homes and people who need a space for a limited time. My domain site is www.vorden-example.com, where is the logo of my company.

Target Market(s)

Companies, entrepreneurs, Companies, entrepreneurs,

Industry/Entity Type

Logistic

Number of Pages Required

5+ page

Colors
0d5aa6
ffffff
000000

Requirements
Must have
• A sober and minimalist homepage type quorbit, NstLoo. That is intuitive, must have spaces for advertising banners. You must always highlight the company logo. A sober and minimalist homepage like quorbit, NstLoo. That is intuitive, must have spaces for advertising banners. Must always highlight the company logo.

```html
<!DOCTYPE html>
<html lang="en">
<head>
<meta charset="utf-8">
<title>VORDEN — Browse All</title>
<link href="https://fonts.googleapis.com/css2?family=Anton&family=Jost:wght@400;500;600&display=swap" rel="stylesheet">
<style>
  :root{
    --brand-blue:#0d5aa6;
    --accent-blue:#2a8bc9;
    --ink:#000000;
    --paper:#ffffff;
    --backdrop:#f3f3f4;
    --rule:#e6e6e6;
    --muted:#7a7a7a;
  }
  *{box-sizing:border-box;margin:0;padding:0}
  html,body{width:1200px;height:1200px;overflow:hidden;background:var(--backdrop)}
  .page-frame{position:absolute;left:45px;top:0;width:1110px;height:1200px;overflow:hidden}
  .page{position:absolute;left:0;top:0;width:1218px;height:1316px;background:var(--paper);
        transform:scale(.9114);transform-origin:0 0;font-family:"Jost",sans-serif;color:var(--ink)}
  .grid-line{position:absolute;top:0;width:1px;background:var(--rule)}
  .header{position:absolute;left:0;top:0;width:100%;height:76px;border-bottom:1px solid var(--rule)}
  .brand{position:absolute;left:10px;top:24px;display:flex;align-items:center;gap:6px}
  .brand-dot{width:28px;height:28px;border-radius:50%;border:2px solid var(--brand-blue)}
  .brand-name{font-family:"Jost",sans-serif;font-weight:600;font-size:17px;color:var(--brand-blue);letter-spacing:1px}
  .search{position:absolute;left:849px;top:30px}
  .menu{position:absolute;left:971px;top:32px;display:flex;align-items:center;gap:14px;font-size:8px;letter-spacing:8px}
  .menu-bars{width:12px;height:6px;border-top:1px solid var(--ink);border-bottom:1px solid var(--ink)}
  .login{position:absolute;left:1157px;top:33px;font-family:"Anton",sans-serif;font-size:10px}
  .page-title{position:absolute;left:272px;top:124px;font-family:"Anton",sans-serif;font-size:27px;letter-spacing:57px;white-space:pre;line-height:1}
  .filters{position:absolute;left:430px;top:208px;display:flex;align-items:center;font-size:13px;font-weight:500}
  .filters .plus{margin-left:18px;margin-right:52px}
  .tag{border:1px solid var(--brand-blue);font-size:8px;padding:2px 6px;margin-right:13px;line-height:11px}
  .listing{position:absolute;width:262px}
  .listing-photo{position:relative;width:262px;height:286px}
  .heart{position:absolute;left:202px;top:22px}
  .photo-aerial{background:linear-gradient(135deg,#5d7a52 0%,#7c8c7a 35%,#b9c6cc 65%,#d5dde0 100%)}
  .photo-hall{background:linear-gradient(180deg,#b8b8b6 0%,#e6e6e4 45%,#f1f1f1 65%,#6f7072 100%)}
  .photo-cafe{background:linear-gradient(180deg,#8a5a3a 0%,#5d4a3c 35%,#8d9692 65%,#3b3a3a 100%)}
  .badge{display:inline-block;margin-top:16px;border:1px solid var(--brand-blue);color:var(--brand-blue);
         font-size:8px;padding:1px 10px;line-height:11px}
  .listing-title{font-family:"Anton",sans-serif;font-weight:400;font-size:25px;line-height:38px;margin-top:4px;white-space:nowrap}
  .price{font-family:"Anton",sans-serif;font-size:23px;color:var(--muted);margin-top:12px;line-height:30px}
  .specs{display:flex;gap:16px;margin-top:10px;font-size:10px;white-space:nowrap}
  .specs b{font-weight:400;font-size:13px}
</style>
</head>
<body>
<div class="page-frame">
<div class="page">
  <span class="grid-line" style="left:207px;height:685px"></span>
  <span class="grid-line" style="left:517px;height:685px"></span>
  <span class="grid-line" style="left:764px;height:685px"></span>
  <span class="grid-line" style="left:929px;height:76px"></span>
  <span class="grid-line" style="left:1115px;height:685px"></span>

  <header class="header">
    <div class="brand"><span class="brand-dot"></span><span class="brand-name">VORDEN</span></div>
    <svg class="search" width="18" height="18" viewBox="0 0 18 18" fill="none" stroke="#000" stroke-width="1.3"><circle cx="10" cy="7.5" r="5.5"/><path d="M6 11.5 2 16"/></svg>
    <div class="menu"><span class="menu-bars"></span><span>MENU</span></div>
    <div class="login">LOGIN</div>
  </header>

  <h1 class="page-title">BROWSE ALL</h1>

  <div class="filters">
    <span>FILTER BY</span><span class="plus">+</span>
    <span class="tag">COMMERCIAL</span><span class="tag">1700sqm</span><span class="tag">CALIFORNIA</span>
  </div>

  <!-- row 1 -->
  <article class="listing" style="left:117px;top:266px">
    <div class="listing-photo photo-aerial" role="img" aria-label="Aerial view of an industrial warehouse roof, parking lot and trees">
      <svg class="heart" width="34" height="30" viewBox="0 0 34 30" fill="none" stroke="#2a8bc9" stroke-width="2"><path d="M17 28 3.5 15A8 8 0 0 1 17 5a8 8 0 0 1 13.5 10Z"/></svg>
    </div>
    <span class="badge">VERIFIED • CALIFORNIA</span>
    <h2 class="listing-title">Industrial warehouse<br>in calefornia</h2>
    <p class="price">$5,000</p>
    <p class="specs"><span><b>4</b> Rooms (Total)</span><span><b>1700</b> Floor Area</span><span><b>1</b> Floors (Total)</span></p>
  </article>
  <article class="listing" style="left:485px;top:266px">
    <div class="listing-photo photo-hall" role="img" aria-label="Empty white warehouse interior with columns and large windows">
      <svg class="heart" width="34" height="30" viewBox="0 0 34 30" fill="none" stroke="#2a8bc9" stroke-width="2"><path d="M17 28 3.5 15A8 8 0 0 1 17 5a8 8 0 0 1 13.5 10Z"/></svg>
    </div>
    <span class="badge">VERIFIED • BARCELONA</span>
    <h2 class="listing-title">Rustic,beachfront<br>warehouse in california</h2>
    <p class="price">$1,000</p>
    <p class="specs"><span><b>4</b> Rooms (Total)</span><span><b>1700</b> Floor Area</span><span><b>1</b> Floors (Total)</span></p>
  </article>
  <article class="listing" style="left:854px;top:266px">
    <div class="listing-photo photo-cafe" role="img" aria-label="Converted warehouse café with wooden ceiling and pendant lamps">
      <svg class="heart" width="34" height="30" viewBox="0 0 34 30" fill="none" stroke="#2a8bc9" stroke-width="2"><path d="M17 28 3.5 15A8 8 0 0 1 17 5a8 8 0 0 1 13.5 10Z"/></svg>
    </div>
    <span class="badge">VERIFIED • BARCELONA</span>
    <h2 class="listing-title">Warehouse near california<br>port</h2>
    <p class="price">$1,000</p>
    <p class="specs"><span><b>4</b> Rooms (Total)</span><span><b>1700</b> Floor Area</span><span><b>1</b> Floors (Total)</span></p>
  </article>

  <!-- row 2 -->
  <article class="listing" style="left:117px;top:793px">
    <div class="listing-photo photo-aerial" role="img" aria-label="Aerial view of an industrial warehouse roof, parking lot and trees">
      <svg class="heart" width="34" height="30" viewBox="0 0 34 30" fill="none" stroke="#2a8bc9" stroke-width="2"><path d="M17 28 3.5 15A8 8 0 0 1 17 5a8 8 0 0 1 13.5 10Z"/></svg>
    </div>
    <span class="badge">VERIFIED • CALIFORNIA</span>
    <h2 class="listing-title">Industrial warehouse<br>in calefornia</h2>
    <p class="price">$5,000</p>
    <p class="specs"><span><b>4</b> Rooms (Total)</span><span><b>1700</b> Floor Area</span><span><b>1</b> Floors (Total)</span></p>
  </article>
  <article class="listing" style="left:485px;top:793px">
    <div class="listing-photo photo-hall" role="img" aria-label="Empty white warehouse interior with columns and large windows">
      <svg class="heart" width="34" height="30" viewBox="0 0 34 30" fill="none" stroke="#2a8bc9" stroke-width="2"><path d="M17 28 3.5 15A8 8 0 0 1 17 5a8 8 0 0 1 13.5 10Z"/></svg>
    </div>
    <span class="badge">VERIFIED • BARCELONA</span>
    <h2 class="listing-title">Rustic,beachfront<br>warehouse in california</h2>
    <p class="price">$1,000</p>
    <p class="specs"><span><b>4</b> Rooms (Total)</span><span><b>1700</b> Floor Area</span><span><b>1</b> Floors (Total)</span></p>
  </article>
  <article class="listing" style="left:854px;top:793px">
    <div class="listing-photo photo-cafe" role="img" aria-label="Converted warehouse café with wooden ceiling and pendant lamps">
      <svg class="heart" width="34" height="30" viewBox="0 0 34 30" fill="none" stroke="#2a8bc9" stroke-width="2"><path d="M17 28 3.5 15A8 8 0 0 1 17 5a8 8 0 0 1 13.5 10Z"/></svg>
    </div>
    <span class="badge">VERIFIED • BARCELONA</span>
    <h2 class="listing-title">Warehouse near california<br>port</h2>
    <p class="price">$1,000</p>
    <p class="specs"><span><b>4</b> Rooms (Total)</span><span><b>1700</b> Floor Area</span><span><b>1</b> Floors (Total)</span></p>
  </article>
</div>
</div>
</body>
</html>
```